Hi,

I would like to have a invitation made for a party. exactly like the picture in the link below.

http://pinboardia.example/pin/529174603381046725/

However, Please change the colors into fun/ girly feeling. font can be different and size of the card should be the same

Name of the girl: RUBA
What: Bachelorette Party
Where:TIKO Boat
Dubai Coral Sails Club
When:7th of February 2013

No RSVP required. (so no need to put it)

```html
<!DOCTYPE html>
<html lang="en">
<head>
<meta charset="utf-8">
<title>Ruba's Bachelorette Party Invitation</title>
<link rel="stylesheet" href="https://fonts.googleapis.com/css2?family=Ewert&family=Rye&family=Sancreek&family=Oswald:wght@300;500&display=swap">
<style>
  :root {
    --card-bg: #4a1b40;
    --panel-fold: #6e3463;
    --headline-pink: #f9b3d2;
    --detail-pink: #f6c6dc;
    --detail-light: #fff0f7;
    --name-white: #ffffff;
    --single-pink: #ff4f9a;
    --ornament-light: #ffd6ec;
    --ornament-deep: #d872b0;
  }
  html, body {
    margin: 0;
    padding: 0;
    width: 1200px;
    height: 552px;
    overflow: hidden;
    background: var(--card-bg);
  }
  .invitation {
    position: relative;
    width: 1200px;
    height: 552px;
    background: var(--card-bg);
    overflow: hidden;
  }
  .fold {
    position: absolute;
    top: 0;
    width: 2px;
    height: 552px;
    background: var(--panel-fold);
  }
  .fold--first { left: 405px; }
  .fold--second { left: 803px; }

  .corner-ornament {
    position: absolute;
    width: 76px;
    height: 69px;
    background: radial-gradient(ellipse at center, var(--ornament-light) 0%, var(--ornament-deep) 55%, rgba(216,114,176,0) 78%);
  }
  .flourish-ornament {
    position: absolute;
    left: 880px;
    top: 486px;
    width: 270px;
    height: 46px;
    background: radial-gradient(ellipse at center, var(--ornament-light) 0%, var(--ornament-deep) 55%, rgba(216,114,176,0) 75%);
  }

  .cover-title {
    position: absolute;
    left: 0;
    top: 0;
    width: 804px;
    height: 552px;
  }
  .cover-title__name {
    font-family: "Rye", serif;
    fill: var(--name-white);
    font-size: 54px;
  }
  .cover-title__tagline {
    font-family: "Sancreek", cursive;
    fill: var(--headline-pink);
    font-size: 56px;
  }
  .cover-title__single {
    font-family: "Ewert", cursive;
    fill: var(--single-pink);
    font-size: 170px;
  }

  .party-details {
    position: absolute;
    left: 805px;
    top: 0;
    width: 395px;
    height: 552px;
    text-align: center;
    font-family: "Oswald", sans-serif;
    text-transform: uppercase;
  }
  .party-details__title {
    position: absolute;
    left: 0;
    width: 100%;
    top: 104px;
    margin: 0;
    font-weight: 500;
    font-size: 19px;
    color: var(--detail-pink);
    letter-spacing: 0.5px;
  }
  .party-details__line {
    position: absolute;
    left: 0;
    width: 100%;
    margin: 0;
    font-weight: 300;
    font-size: 16px;
    line-height: 22px;
    color: var(--detail-pink);
    letter-spacing: 0.5px;
  }
  .party-details__line--joiner { color: var(--detail-light); font-weight: 500; }
</style>
</head>
<body>
<main class="invitation">
  <div class="fold fold--first"></div>
  <div class="fold fold--second"></div>

  <div class="corner-ornament" role="img" aria-label="Filigree corner ornament" style="left:10px;top:10px"></div>
  <div class="corner-ornament" role="img" aria-label="Filigree corner ornament" style="left:325px;top:10px"></div>
  <div class="corner-ornament" role="img" aria-label="Filigree corner ornament" style="left:415px;top:10px"></div>
  <div class="corner-ornament" role="img" aria-label="Filigree corner ornament" style="left:724px;top:10px"></div>
  <div class="corner-ornament" role="img" aria-label="Filigree corner ornament" style="left:811px;top:10px"></div>
  <div class="corner-ornament" role="img" aria-label="Filigree corner ornament" style="left:1116px;top:10px"></div>

  <div class="corner-ornament" role="img" aria-label="Filigree corner ornament" style="left:10px;top:472px"></div>
  <div class="corner-ornament" role="img" aria-label="Filigree corner ornament" style="left:325px;top:472px"></div>
  <div class="corner-ornament" role="img" aria-label="Filigree corner ornament" style="left:415px;top:472px"></div>
  <div class="corner-ornament" role="img" aria-label="Filigree corner ornament" style="left:724px;top:472px"></div>
  <div class="corner-ornament" role="img" aria-label="Filigree corner ornament" style="left:811px;top:472px"></div>
  <div class="corner-ornament" role="img" aria-label="Filigree corner ornament" style="left:1116px;top:472px"></div>

  <div class="flourish-ornament" role="img" aria-label="Scrolling flourish divider"></div>

  <svg class="cover-title" viewBox="0 0 804 552" xmlns="http://www.w3.org/2000/svg">
    <title>Ruba's last chance to celebrate being single</title>
    <defs>
      <filter id="name-shadow" x="-10%" y="-20%" width="130%" height="160%">
        <feDropShadow dx="5" dy="5" stdDeviation="3" flood-color="#1a0716" flood-opacity="0.85"/>
      </filter>
    </defs>
    <text class="cover-title__name" x="70" y="170" textLength="280" lengthAdjust="spacingAndGlyphs" filter="url(#name-shadow)">RUBA’S</text>
    <text class="cover-title__tagline" x="30" y="262" textLength="345" lengthAdjust="spacingAndGlyphs">LAST CHANCE TO</text>
    <text class="cover-title__tagline" x="416" y="262" textLength="360" lengthAdjust="spacingAndGlyphs">CELEBRATE BEING</text>
    <text class="cover-title__single" x="30" y="448" textLength="748" lengthAdjust="spacingAndGlyphs">SINGLE</text>
  </svg>

  <section class="party-details">
    <h1 class="party-details__title">Bachelorette Party</h1>
    <p class="party-details__line party-details__line--joiner" style="top:176px">At</p>
    <p class="party-details__line" style="top:204px">TIKO Boat</p>
    <p class="party-details__line" style="top:262px">Dubai Coral Sails Club</p>
    <p class="party-details__line party-details__line--joiner" style="top:302px">On</p>
    <p class="party-details__line" style="top:345px">7th of February 2013</p>
  </section>
</main>
</body>
</html>
```